Logo and 1 page Flyer for Meridian Fund

We need a logo and a 1 single page flyer for an Investment Fund we'll distribute worldwide. It'a Meridian Fund that will give a return also to the poorest people in the world. Details inside. We give just an idea (based on a previous flyer we had here) with the attached draft. Anyone can figure out how to make its own. NOTE: LQV is our company's logo.

Target Market(s)

Investors

Industry/Entity Type

Finance And Accounting

Logo Text

KOLB Kindred Open Bloom Fund

Font styles to use
Serif

Colors
00a990

Requirements
Must have
• A logo you choose which should be:
• - Elegant
• - Innovative
• - Crypto evoking (Company launching is a cripto company)
• - Hi tech
Nice to have
• We have sent you all materials to be able to understand:
• 1. A draft of how we would like the texts to come out. Don't use this (we're already using with other texts), ,but see the evidence of Logo, Slogan, and the 3 main characteristics. Also notice very well that is very elegant. Use a real light on color, make it as shining as you can. It must be a sort of shining green, expressing Hope, Beauty, Well being
• 2. The logo for LQV that is the company launching the project. In draft you see on low left. You can put wherever you feel right
• 3. All texts are on draft to be seen, and on word to be used. You can choose font and dimensions as you prefer
• 4. We've given you logo we have for PIRO. If you feel, you can use in the line where we talk about it or place somewhere. Not mandatory
Should not have
• Funny things; too commercial style; unprofessional aspect

```html
<!DOCTYPE html>
<html lang="en">
<head>
<meta charset="utf-8">
<title>KOLB – Kindred Open Bloom Fund</title>
<link href="https://fonts.googleapis.com/css2?family=Libre+Baskerville:wght@700&family=Mulish:wght@400;700;800&display=swap" rel="stylesheet">
<style>
  :root{
    --navy:#04142e;
    --navy-deep:#010814;
    --network-blue:#0d4f9c;
    --teal:#00a990;
    --teal-dark:#007a66;
    --teal-light:#16c9a8;
    --brand-blue:#1f3f8f;
    --ink:#2e2e2e;
    --label:#0b7a63;
    --paper:#ffffff;
    --mist:#e6eaee;
  }
  *{box-sizing:border-box;margin:0;padding:0}
  html,body{width:1200px;height:1200px;overflow:hidden;background:var(--paper)}
  .flyer{position:relative;width:1200px;height:1200px;background:var(--paper);font-family:"Mulish",sans-serif;color:var(--ink);overflow:hidden}
  .tower-photo{position:absolute;left:0;top:820px;width:1200px;height:380px;
    background:radial-gradient(ellipse 560px 360px at 360px 380px,var(--mist) 0%,rgba(230,234,238,.6) 55%,rgba(255,255,255,0) 100%)}
  .header-art{position:absolute;left:0;top:0;width:1200px;height:560px}
  .fund-badge{position:absolute;left:85px;top:222px;width:362px;height:362px;border-radius:50%;
    background:var(--paper);border:11px solid var(--teal);display:flex;flex-direction:column;
    align-items:center;justify-content:center;box-shadow:0 6px 18px rgba(0,0,0,.18)}
  .fund-badge .brand-row{display:flex;align-items:center;gap:12px}
  .fund-badge .brand-dot{width:40px;height:40px;border-radius:50%;background:var(--brand-blue)}
  .fund-badge .brand-name{font-family:"Libre Baskerville",serif;font-weight:700;font-size:58px;color:var(--brand-blue);line-height:1}
  .fund-badge .brand-full{font-family:"Libre Baskerville",serif;font-weight:700;font-size:19px;color:var(--brand-blue);margin-top:14px;text-align:center;line-height:1.3}
  .slogan{position:absolute;left:0;top:598px;width:1200px;text-align:center;font-size:29px;line-height:40px;color:var(--ink)}
  .features{position:absolute;left:105px;top:755px;width:992px;height:290px;border-radius:42px;
    background:rgba(255,255,255,.78);border:2px solid #fff;box-shadow:0 2px 10px rgba(0,0,0,.18)}
  .feature{position:absolute;left:50px;right:40px;display:flex;align-items:center}
  .feature-label{width:278px;font-weight:800;font-size:22px;color:var(--label);letter-spacing:.2px}
  .feature-text{border-left:2px dashed #444;padding-left:22px;font-size:21px;line-height:25px;color:var(--ink)}
  .site-footer{position:absolute;left:0;top:1114px;width:820px;height:40px;display:flex;align-items:center;gap:20px}
  .footer-rule{height:10px;background:var(--teal)}
  .footer-rule.lead{width:90px;flex:none}
  .footer-rule.trail{flex:1}
  .site{flex:none;font-weight:800;font-size:27px;line-height:40px;color:#1a1a1a;white-space:nowrap}
  .maker{position:absolute;left:840px;top:1078px;display:flex;align-items:center;gap:16px}
  .maker .maker-dot{width:92px;height:92px;border-radius:50%;background:var(--brand-blue)}
  .maker .maker-name{font-family:"Mulish",sans-serif;font-weight:800;font-size:84px;color:var(--brand-blue);line-height:1}
</style>
</head>
<body>
<div class="flyer">
  <div class="tower-photo" role="img" aria-label="Faint photograph of a modern office tower fading into white"></div>

  <svg class="header-art" viewBox="0 0 1200 560">
    <defs>
      <linearGradient id="bandGrad" x1="0" y1="0" x2="1" y2="0">
        <stop offset="0" stop-color="#007a66"/>
        <stop offset=".55" stop-color="#16c9a8"/>
        <stop offset="1" stop-color="#007a66"/>
      </linearGradient>
      <radialGradient id="netGrad" cx=".55" cy=".85" r=".8">
        <stop offset="0" stop-color="#0d4f9c"/>
        <stop offset=".5" stop-color="#04142e"/>
        <stop offset="1" stop-color="#010814"/>
      </radialGradient>
    </defs>
    <path class="teal-band" d="M0,70 C90,380 270,545 520,545 C820,545 1090,400 1200,220 V20 H0 Z" fill="url(#bandGrad)"/>
    <path class="network-field" role="img" aria-label="Dark blue digital network of glowing dots and lines"
          d="M0,0 H1200 V25 C1110,300 820,488 470,488 C260,488 90,360 0,80 Z" fill="url(#netGrad)"/>
  </svg>

  <div class="fund-badge">
    <div class="brand-row"><span class="brand-dot"></span><span class="brand-name">KOLB</span></div>
    <div class="brand-full">Kindred Open Bloom Fund</div>
  </div>

  <p class="slogan">Raise the Poor surfing with us<br>With KOLB you achieve sound return on your investment.<br>And you help needy ones to obtain real help in their life.</p>

  <section class="features">
    <div class="feature" style="top:32px">
      <span class="feature-label">BETTER RETURN</span>
      <span class="feature-text">Using PIRO – Highly AdavancedTrading System.<br>A breaktrough in money management</span>
    </div>
    <div class="feature" style="top:115px">
      <span class="feature-label">FOR ANYONE</span>
      <span class="feature-text">For those who can invest. And for those Who<br>have no money to survive.</span>
    </div>
    <div class="feature" style="top:196px">
      <span class="feature-label">MONEY AND HEARTH</span>
      <span class="feature-text" style="padding-top:12px;padding-bottom:12px">To have a return that Warms you and others.</span>
    </div>
  </section>

  <footer class="site-footer">
    <span class="footer-rule lead"></span>
    <span class="site">www.lqvfund.io</span>
    <span class="footer-rule trail"></span>
  </footer>

  <div class="maker"><span class="maker-dot"></span><span class="maker-name">LQV</span></div>
</div>
</body>
</html>
```